Haulage company, lets use ruby red white and some 3rd color for web design. and Peter Holloway Transport logo

Target Market(s)

Transport industry

Industry/Entity Type

transport

Number of Pages Required

2 page

Requirements
Must have
• Logo

```html
<!DOCTYPE html>
<html lang="en">
<head>
<meta charset="utf-8">
<title>Peter Holloway Transport</title>
<link href="https://fonts.googleapis.com/css2?family=Audiowide&family=Roboto:ital,wght@0,400;0,500;0,700;1,400&display=swap" rel="stylesheet">
<style>
:root{
  --ruby:#d6093b;
  --ruby-dark:#5b1626;
  --ink:#111111;
  --night:#0b0b0b;
  --charcoal:#2b2b2b;
  --white:#ffffff;
  --muted:#666666;
  --teal:#1f7a8c;
  --line:#e3e3e3;
}
*{margin:0;padding:0;box-sizing:border-box}
html,body{width:1200px;height:3372px;overflow:hidden}
body{position:relative;font-family:"Roboto",Arial,sans-serif;color:var(--ink);background:var(--white)}
.abs{position:absolute}
.display{font-family:"Audiowide","Roboto",sans-serif;font-weight:400}
.logo{line-height:1}
.logo .top{color:var(--white);display:block}
.logo .bottom{color:var(--ruby);display:block}

/* header */
.site-header{left:0;top:0;width:1200px;height:70px;background:var(--night)}
.site-header .logo{left:107px;top:13px;font-size:21px}
.nav{left:0;top:26px;font-size:14px;font-weight:700;color:var(--white)}
.nav span{position:absolute;white-space:nowrap}
.nav .active{color:var(--ruby)}
.btn{display:flex;align-items:center;justify-content:center;gap:5px;background:var(--ruby);color:var(--white);font-weight:700;border-radius:22px;font-size:14px}
.btn svg{width:13px;height:13px}
.btn-start{left:941px;top:16px;width:145px;height:41px}

/* hero */
.hero{left:0;top:70px;width:1200px;height:670px;background:linear-gradient(180deg,#7d8a99 0%,#5f6d7d 35%,#4a4f55 60%,#5a5a55 100%)}
.hero-welcome{left:111px;top:200px;font-size:25px;color:var(--white)}
.hero-title{left:107px;top:240px;font-size:80px;line-height:82px}
.hero-title .top{color:var(--white)}
.hero-title .bottom{color:var(--ruby)}
.btn-quote{left:115px;top:424px;width:147px;height:39px;font-size:14px}
.hero-arrow{width:44px;height:44px;border-radius:50%;background:rgba(255,255,255,.25);border:1px solid rgba(255,255,255,.5);display:flex;align-items:center;justify-content:center}

.feature-card{top:595px;width:318px;height:261px;border-radius:16px;border:4px solid var(--white);overflow:hidden}
.feature-card.photo{background:linear-gradient(180deg,#b9c3cc 0%,#9aa3a9 45%,#5e5553 75%,#3b3436 100%)}
.feature-card .label{position:absolute;left:0;right:0;bottom:40px;text-align:center;color:var(--white);font-size:20px;font-weight:700}
.feature-card.accent{background:linear-gradient(180deg,var(--ruby) 0%,#a80f35 45%,var(--ruby-dark) 100%);color:var(--white);text-align:center}
.feature-card.accent h3{margin-top:64px;font-size:20px;font-weight:700}
.feature-card.accent p{margin:18px 34px 0;font-size:14px;line-height:21px;text-align:justify;text-align-last:center}
.feature-card.accent .more{margin-top:24px;font-size:13px;font-weight:700;display:flex;justify-content:center;align-items:center;gap:5px}

/* section headings */
.section-title{left:0;width:1200px;text-align:center;font-size:31px}

/* clients */
.client{top:1014px;width:183px;height:98px;border-radius:12px;background:var(--white);box-shadow:0 2px 10px rgba(0,0,0,.12);display:flex;align-items:center;justify-content:center;gap:8px;font-size:14px;font-weight:700;color:#333}
.client i{width:12px;height:12px;background:#333;display:block;flex:none}

/* highlights */
.highlights{left:0;top:1204px;width:1200px;height:652px;background:var(--charcoal)}
.hl-title{font-size:17px;font-weight:700;color:var(--white)}
.hl-text{font-size:13px;line-height:20.5px;color:var(--white);margin-top:13px}
.hl-left{width:260px;text-align:right}
.hl-right{width:260px;text-align:left}
.hl-icon{width:82px;height:56px}
.hub{left:458px;top:1432px;width:284px;height:284px;border-radius:50%;background:var(--white)}
.hub-photo{left:480px;top:1454px;width:240px;height:240px;border-radius:50%;background:linear-gradient(180deg,#c8cdd1 0%,#a7adb2 50%,#5f6a5a 75%,#8d8d89 100%)}

/* testimonials */
.testimonials{left:0;top:1856px;width:1200px;height:473px;background:radial-gradient(circle at 30% 40%,#e0194c 0%,var(--ruby) 50%,#c8073a 100%)}
.quote-card{top:2039px;width:314px;height:214px;background:var(--white);border-radius:6px}
.quote-card p{position:absolute;left:30px;top:66px;width:262px;font-size:13.5px;line-height:21px;font-style:italic;color:#555}
.quote-card .who{position:absolute;left:32px;top:168px;font-size:17px;color:var(--teal)}
.quote-card .who small{font-size:13px;color:#555;margin-left:8px}
.quote-card .mark{position:absolute;right:18px;bottom:-24px;font-family:"Audiowide",sans-serif;font-size:60px;line-height:1;color:var(--ruby)}
.avatar{width:92px;height:92px;border-radius:50%;background:linear-gradient(180deg,#c9c3bd 0%,#9b8a7c 100%);border:3px solid var(--white)}
.round-arrow{width:45px;height:45px;border-radius:50%;background:rgba(255,255,255,.3);border:1px solid rgba(255,255,255,.6);display:flex;align-items:center;justify-content:center}

/* blog */
.post{top:2490px;width:315px;height:395px;border:1px solid var(--line);background:var(--white)}
.post .thumb{height:210px;background:linear-gradient(180deg,#7f8a96 0%,#aeb3b6 45%,#8d7b77 75%,#4a4444 100%)}
.post h3{margin:24px 20px 0;font-size:16.5px;line-height:24px;font-weight:700}
.post .meta{margin:16px 20px 0;font-size:12.5px;color:#666;display:flex;align-items:center;gap:8px}
.post .meta svg{width:11px;height:11px}
.post p{margin:16px 20px 0;font-size:14px;line-height:22px;color:#666}

/* footer */
.site-footer{left:0;top:3000px;width:1200px;height:372px;background:var(--charcoal);color:var(--white)}
.foot-logo{left:107px;top:3093px;font-size:22px}
.foot-head{top:3093px;font-size:18px;font-weight:700;color:var(--ruby)}
.foot-list{font-size:14px;line-height:26px}
.foot-list li{list-style:none;display:flex;align-items:center;gap:14px}
.foot-list svg{width:10px;height:10px;flex:none}
.contact li{align-items:flex-start;gap:16px}
.social{top:3136px;width:42px;height:42px;background:var(--white);color:var(--ruby);font-size:10px;font-weight:700;display:flex;align-items:center;justify-content:center}
.dash{left:0;top:3289px;width:1200px;border-top:1px dashed rgba(255,255,255,.6)}
.go-up{left:1008px;top:3278px;width:80px;height:22px;border-radius:11px;background:var(--ruby);font-size:11px;font-weight:700;display:flex;align-items:center;justify-content:center;gap:4px}
.copyright{left:0;top:3320px;width:1200px;text-align:center;font-size:14px}
</style>
</head>
<body>

<header class="abs site-header">
  <div class="abs logo display"><span class="top">Peter Holloway</span><span class="bottom">Transport</span></div>
  <nav class="abs nav">
    <span class="active" style="left:378px">Home</span>
    <span style="left:457px">Service</span>
    <span style="left:546px">Equipment</span>
    <span style="left:656px">Preise</span>
    <span style="left:738px">Uber Uns</span>
    <span style="left:838px">Kontakt</span>
  </nav>
  <div class="abs btn btn-start">GET STARTED <svg viewBox="0 0 16 16"><circle cx="8" cy="8" r="8" fill="#fff"/><path d="M6 4l4 4-4 4" stroke="#d6093b" stroke-width="2.2" fill="none"/></svg></div>
</header>

<section class="abs hero" role="img" aria-label="Photo of a red and white articulated lorry parked on a coastal road"></section>
<div class="abs hero-welcome display">Welcome to</div>
<h1 class="abs hero-title display logo"><span class="top">Peter Holloway</span><span class="bottom">Transport</span></h1>
<div class="abs btn btn-quote">GET A QUOTE <svg viewBox="0 0 16 16"><circle cx="8" cy="8" r="8" fill="#fff"/><path d="M6 4l4 4-4 4" stroke="#d6093b" stroke-width="2.2" fill="none"/></svg></div>
<div class="abs hero-arrow" style="left:1122px;top:338px"><svg width="14" height="14" viewBox="0 0 14 14"><path d="M3 9l4-4 4 4" stroke="#333" stroke-width="1.6" fill="none"/></svg></div>
<div class="abs hero-arrow" style="left:1122px;top:390px"><svg width="14" height="14" viewBox="0 0 14 14"><path d="M3 5l4 4 4-4" stroke="#fff" stroke-width="1.6" fill="none"/></svg></div>

<div class="abs feature-card photo" style="left:105px" role="img" aria-label="Photo of a lorry on a wet road"><span class="label">Lorem ipsum</span></div>
<div class="abs feature-card accent" style="left:441px">
  <h3>Lorem ipsum</h3>
  <p>Sed ut perspiciatis unde omnis iste natus error sit voluptat accusantium doloremque laudantium</p>
  <div class="more">LEARN MORE <svg width="13" height="13" viewBox="0 0 16 16"><circle cx="8" cy="8" r="8" fill="#fff"/><path d="M6 4l4 4-4 4" stroke="#8a1030" stroke-width="2.2" fill="none"/></svg></div>
</div>
<div class="abs feature-card photo" style="left:776px" role="img" aria-label="Photo of two lorries parked side by side"><span class="label">Lorem ipsum</span></div>

<h2 class="abs section-title display" style="top:946px">Our Clients</h2>
<div class="abs client" style="left:111px"><i></i>Swiftline Cargo</div>
<div class="abs client" style="left:310px"><i></i>Northway Freight</div>
<div class="abs client" style="left:509px"><i></i>Ironroad Haul</div>
<div class="abs client" style="left:708px"><i></i>Keel Delivery</div>
<div class="abs client" style="left:906px"><i></i>Brightmile Logistics</div>

<section class="abs highlights"></section>
<h2 class="abs section-title display" style="top:1299px;color:var(--white)">Our Highlights</h2>
<svg class="abs" style="left:0;top:1204px" width="1200" height="652" viewBox="0 0 1200 652">
  <g stroke="#fff" stroke-width="1.3" fill="none">
    <path d="M398 300v50h60"/><path d="M398 420v-45h60"/>
    <path d="M796 300v50h-58"/><path d="M796 420v-45h-58"/>
  </g>
  <g fill="#d6093b">
    <!-- truck icons -->
    <g transform="translate(360,204)"><rect x="0" y="4" width="48" height="32" rx="3"/><path d="M50 12h16l14 14v10H50z"/><circle cx="14" cy="40" r="7" stroke="#2b2b2b" stroke-width="3"/><circle cx="64" cy="40" r="7" stroke="#2b2b2b" stroke-width="3"/><rect x="-6" y="12" width="18" height="3"/><rect x="-10" y="20" width="18" height="3"/></g>
    <g transform="translate(759,204)"><rect x="0" y="0" width="44" height="34" rx="2"/><path d="M46 12h14l12 12v12H46z"/><circle cx="14" cy="40" r="6" stroke="#2b2b2b" stroke-width="3"/><circle cx="62" cy="40" r="6" stroke="#2b2b2b" stroke-width="3"/></g>
    <g transform="translate(370,436)"><path d="M10 14l6-12h30l6 12h4v20h-6v8h-8v-8H20v8h-8v-8H6V14z"/><rect x="20" y="6" width="22" height="8" fill="#2b2b2b"/><circle cx="16" cy="24" r="3" fill="#2b2b2b"/><circle cx="46" cy="24" r="3" fill="#2b2b2b"/></g>
    <g transform="translate(759,438)"><rect x="0" y="0" width="44" height="32" rx="3"/><path d="M46 10h14l12 12v10H46z"/><circle cx="14" cy="38" r="7" stroke="#2b2b2b" stroke-width="3"/><circle cx="62" cy="38" r="7" stroke="#2b2b2b" stroke-width="3"/></g>
  </g>
</svg>
<div class="abs hub"></div>
<div class="abs hub-photo" role="img" aria-label="Photo of a lorry cab seen head-on"></div>

<div class="abs hl-left" style="left:69px;top:1407px"><div class="hl-title">Personal advice</div><div class="hl-text">At vero eos et accusamus et<br>iusto odio dignissimos ducimus<br>qui blanditiis</div></div>
<div class="abs hl-right" style="left:869px;top:1407px"><div class="hl-title">Mixture customer &amp; moverich</div><div class="hl-text">At vero eos et accusamus et<br>iusto odio dignissimos ducimus<br>qui blanditiis</div></div>
<div class="abs hl-left" style="left:69px;top:1638px"><div class="hl-title">Special moving goods</div><div class="hl-text">At vero eos et accusamus et<br>iusto odio dignissimos ducimus<br>qui blanditiis</div></div>
<div class="abs hl-right" style="left:869px;top:1638px"><div class="hl-title">No min order</div><div class="hl-text">At vero eos et accusamus et<br>iusto odio dignissimos ducimus<br>qui blanditiis</div></div>

<section class="abs testimonials"></section>
<h2 class="abs section-title display" style="top:1919px;color:var(--white)">What Our Clients Say</h2>
<div class="abs round-arrow" style="left:33px;top:2127px"><svg width="12" height="12" viewBox="0 0 12 12"><path d="M8 2L4 6l4 4" stroke="#fff" stroke-width="1.5" fill="none"/></svg></div>
<div class="abs round-arrow" style="left:1124px;top:2127px"><svg width="12" height="12" viewBox="0 0 12 12"><path d="M4 2l4 4-4 4" stroke="#fff" stroke-width="1.5" fill="none"/></svg></div>

<div class="abs quote-card" style="left:111px"><p>Lorem ipsum dolor sit amet, consectetur adipiscing elit, sed do eiusmod tempor incididunt ut labore et dolore magna aliqua. Ut enim ad minim veniam</p><div class="who">John doe<small>Company name</small></div><div class="mark">”</div></div>
<div class="abs quote-card" style="left:443px"><p>Lorem ipsum dolor sit amet, consectetur adipiscing elit, sed do eiusmod tempor incididunt ut labore et dolore magna aliqua. Ut enim ad minim veniam</p><div class="who">John doe<small>Company name</small></div><div class="mark">”</div></div>
<div class="abs quote-card" style="left:775px"><p>Lorem ipsum dolor sit amet, consectetur adipiscing elit, sed do eiusmod tempor incididunt ut labore et dolore magna aliqua. Ut enim ad minim veniam</p><div class="who">John doe<small>Company name</small></div><div class="mark">”</div></div>
<div class="abs avatar" style="left:139px;top:1991px" role="img" aria-label="Portrait photo of a client"></div>
<div class="abs avatar" style="left:471px;top:1991px" role="img" aria-label="Portrait photo of a client"></div>
<div class="abs avatar" style="left:803px;top:1991px;background:linear-gradient(180deg,#bcd3e6 0%,#7e93a8 100%)" role="img" aria-label="Portrait photo of a client"></div>

<h2 class="abs section-title display" style="top:2408px">Latest Blog</h2>
<svg class="abs" style="left:44px;top:2676px" width="20" height="28" viewBox="0 0 20 28"><path d="M15 3L5 14l10 11" stroke="#111" stroke-width="2.6" fill="none"/></svg>
<svg class="abs" style="left:1134px;top:2676px" width="20" height="28" viewBox="0 0 20 28"><path d="M5 3l10 11-10 11" stroke="#111" stroke-width="2.6" fill="none"/></svg>

<article class="abs post" style="left:107px">
  <div class="thumb" role="img" aria-label="Night photo of two lorries in a yard" style="background:linear-gradient(180deg,#1d1f22 0%,#3a3733 45%,#8b7a70 70%,#2a2625 100%)"></div>
  <h3>Sed ut perspiciatis unde omnis iste natus</h3>
  <div class="meta"><svg viewBox="0 0 12 12"><rect x="1" y="2" width="10" height="9" fill="#d6093b"/></svg>May 2022 &nbsp;&nbsp;| &nbsp;&nbsp;<svg viewBox="0 0 12 12"><circle cx="6" cy="3.5" r="2.5" fill="#d6093b"/><path d="M1 12a5 5 0 0110 0z" fill="#d6093b"/></svg>Alan Mercer</div>
  <p>Lorem ipsum dolor sit amet, consectetur adipiscing elit, sed do eiusmod</p>
</article>
<article class="abs post" style="left:443px">
  <div class="thumb" role="img" aria-label="Photo of two lorries parked on wet tarmac"></div>
  <h3>Sed ut perspiciatis unde omnis iste natus</h3>
  <div class="meta"><svg viewBox="0 0 12 12"><rect x="1" y="2" width="10" height="9" fill="#d6093b"/></svg>May 2022 &nbsp;&nbsp;| &nbsp;&nbsp;<svg viewBox="0 0 12 12"><circle cx="6" cy="3.5" r="2.5" fill="#d6093b"/><path d="M1 12a5 5 0 0110 0z" fill="#d6093b"/></svg>Alan Mercer</div>
  <p>Lorem ipsum dolor sit amet, consectetur adipiscing elit, sed do eiusmod</p>
</article>
<article class="abs post" style="left:778px">
  <div class="thumb" role="img" aria-label="Dusk photo of a lorry cab" style="background:linear-gradient(180deg,#6f88b0 0%,#b7a79d 45%,#7b2b36 70%,#2f2b2c 100%)"></div>
  <h3>Sed ut perspiciatis unde omnis iste natus</h3>
  <div class="meta"><svg viewBox="0 0 12 12"><rect x="1" y="2" width="10" height="9" fill="#d6093b"/></svg>May 2022 &nbsp;&nbsp;| &nbsp;&nbsp;<svg viewBox="0 0 12 12"><circle cx="6" cy="3.5" r="2.5" fill="#d6093b"/><path d="M1 12a5 5 0 0110 0z" fill="#d6093b"/></svg>Alan Mercer</div>
  <p>Lorem ipsum dolor sit amet, consectetur adipiscing elit, sed do eiusmod</p>
</article>

<footer class="abs site-footer"></footer>
<div class="abs foot-logo logo display"><span class="top">Peter Holloway</span><span class="bottom">Transport</span></div>

<div class="abs foot-head" style="left:408px">Links</div>
<ul class="abs foot-list" style="left:408px;top:3131px">
  <li><svg viewBox="0 0 10 10"><path d="M1 2l3 3-3 3M5 2l3 3-3 3" stroke="#fff" stroke-width="1.4" fill="none"/></svg>Home</li>
  <li><svg viewBox="0 0 10 10"><path d="M1 2l3 3-3 3M5 2l3 3-3 3" stroke="#fff" stroke-width="1.4" fill="none"/></svg>About us</li>
  <li><svg viewBox="0 0 10 10"><path d="M1 2l3 3-3 3M5 2l3 3-3 3" stroke="#fff" stroke-width="1.4" fill="none"/></svg>Services</li>
  <li><svg viewBox="0 0 10 10"><path d="M1 2l3 3-3 3M5 2l3 3-3 3" stroke="#fff" stroke-width="1.4" fill="none"/></svg>Token Sale</li>
</ul>

<div class="abs foot-head" style="left:622px">Contact us</div>
<ul class="abs foot-list contact" style="left:624px;top:3128px">
  <li><svg viewBox="0 0 10 10" style="margin-top:8px"><path d="M5 10L1.5 4.5A3.5 3.5 0 118.5 4.5z" fill="#fff"/><circle cx="5" cy="3.6" r="1.3" fill="#2b2b2b"/></svg><span>Lorem ipsum dolor sit amet,<br>consectetur adipiscing</span></li>
  <li><svg viewBox="0 0 10 10" style="margin-top:8px"><path d="M2 0l2 2.5-1.2 1.5a6 6 0 003.2 3.2L7.5 6 10 8l-1.5 2C4 10 0 6 0 1.5z" fill="#fff"/></svg><span>+1 888 888 8888</span></li>
  <li><svg viewBox="0 0 10 10" style="margin-top:8px"><rect x="0" y="1.5" width="10" height="7" fill="#fff"/><path d="M0 1.5l5 4 5-4" stroke="#2b2b2b" fill="none"/></svg><span>info@hollowayhaul.com</span></li>
</ul>

<div class="abs foot-head" style="left:890px">Connect With Us</div>
<div class="abs social" style="left:894px">Frendo</div>
<div class="abs social" style="left:944px">Vidzy</div>
<div class="abs social" style="left:994px">Pixa</div>
<div class="abs social" style="left:1044px">Wrkd</div>

<div class="abs dash"></div>
<div class="abs go-up" style="color:var(--white)"><svg width="9" height="9" viewBox="0 0 10 10"><path d="M5 1L1 5h2.5v4h3V5H9z" fill="#fff"/></svg>Go Up</div>
<div class="abs copyright" style="color:var(--white)">© 2024 Company name | All Rights Reserved</div>

</body>
</html>
```